Business cards for a naturopathic day clinic for stem cell therapy

We need a basic design for a day clinic, that offers stem cell therapies for Lyme therapy and other severe chronic illnesses.
Our name is "Casa velorìn", which can be translated into "Manor Velorbloom". We are a couple of naturopaths working along side physiotherapists and osteopaths, yoga teachers and massage therapists. I attached our logo.

```html
<!DOCTYPE html>
<html lang="en">
<head>
<meta charset="utf-8">
<title>Manor Velorbloom — Business Cards</title>
<link href="https://fonts.googleapis.com/css2?family=Montserrat:wght@300;400;500&display=swap" rel="stylesheet">
<style>
  :root {
    --leaf: #b9c563;
    --bark: #8a7868;
    --bark-band: #a79686;
    --paper: #ffffff;
    --backdrop: #3b3936;
  }
  * { margin: 0; padding: 0; box-sizing: border-box; }
  html, body { width: 1200px; height: 900px; overflow: hidden; }
  body {
    background: var(--backdrop);
    font-family: "Montserrat", sans-serif;
    display: flex; flex-direction: column; align-items: center; justify-content: center;
    gap: 56px;
  }
  .card {
    width: 665px; height: 380px; position: relative; overflow: hidden;
    box-shadow: 0 10px 30px rgba(0,0,0,.45);
  }
  .card--front { background: var(--leaf); display: flex; align-items: center; justify-content: center; }
  .card--back { background: var(--paper); }

  .brand { display: flex; align-items: center; gap: 18px; }
  .brand__dot { border-radius: 50%; flex: none; }
  .brand__name { font-weight: 300; letter-spacing: 2px; white-space: nowrap; }
  .card--front .brand__dot { width: 76px; height: 76px; border: 3px solid var(--paper); }
  .card--front .brand__name { color: var(--paper); font-size: 44px; }

  .card--back .brand { position: absolute; top: 46px; right: 40px; gap: 12px; }
  .card--back .brand__dot { width: 48px; height: 48px; background: var(--leaf); }
  .card--back .brand__name { color: var(--bark); font-size: 28px; }

  .divider { position: absolute; height: 1px; background: var(--bark); }
  .divider--wide { left: 40px; right: 40px; top: 170px; }
  .divider--short { left: 40px; width: 250px; top: 246px; }

  .person { position: absolute; left: 40px; top: 190px; color: var(--bark); }
  .person__name { font-size: 22px; font-weight: 400; letter-spacing: 2px; text-transform: uppercase; }
  .person__role { font-size: 14px; margin-top: 4px; color: #6e6258; }

  .contacts { position: absolute; left: 40px; top: 262px; list-style: none; color: #4a423c; font-size: 14px; }
  .contacts li { display: flex; align-items: center; gap: 10px; height: 24px; }
  .contacts svg { width: 14px; height: 14px; fill: var(--leaf); flex: none; }

  .address { position: absolute; right: 40px; top: 200px; text-align: right; color: #4a423c; font-size: 14px; line-height: 1.6; }

  .band { position: absolute; left: 0; right: 0; bottom: 0; height: 10px; background: var(--bark-band); }
  .web-tab {
    position: absolute; right: 0; bottom: 0; width: 250px; height: 40px; background: var(--leaf);
    color: var(--paper); font-size: 14px; font-weight: 500;
    display: flex; align-items: center; justify-content: center;
  }
</style>
</head>
<body>
  <section class="card card--front">
    <div class="brand">
      <span class="brand__dot"></span>
      <span class="brand__name">Manor Velorbloom</span>
    </div>
  </section>

  <section class="card card--back">
    <div class="brand">
      <span class="brand__dot"></span>
      <span class="brand__name">Manor Velorbloom</span>
    </div>
    <div class="divider divider--wide"></div>

    <div class="person">
      <p class="person__name">Jonas Ferrell</p>
      <p class="person__role">President</p>
    </div>
    <div class="divider divider--short"></div>

    <ul class="contacts">
      <li><svg viewBox="0 0 16 16" aria-hidden="true"><path d="M3.5 1l2.5 3-1.5 1.8a9 9 0 0 0 5.7 5.7L12 10l3 2.5-1.5 2.5C7 15 1 9 1 2.5z"/></svg>+49 6150 3817206</li>
      <li><svg viewBox="0 0 16 16" aria-hidden="true"><path d="M4 1h8v4H4zM1 6h14v6h-3v3H4v-3H1zM5 10v4h6v-4z"/></svg>06150 5140937</li>
      <li><svg viewBox="0 0 16 16" aria-hidden="true"><path d="M1 3h14v1L8 9 1 4zM1 6l7 5 7-5v7H1z"/></svg>info@casa-velorin.de</li>
    </ul>

    <address class="address" style="font-style:normal">
      Lindenweg 7<br>64850 Talheim, Germany
    </address>

    <div class="band"></div>
    <div class="web-tab">www.casa-velorin.de</div>
  </section>
</body>
</html>
```